Valorix Stationery
Letterhead and business card
I need double sided standard sized Business Card [3.5" x 2"]
Anything
Professional
Marla Greene
Professional Engineer
4817 North 52nd Avenue
Tulsa, OK 74068
918.6273.PRO
marla@valorix-example.com
http://valorix-example.com
Tagline "We keep your project moving"
Valorix logo chosen from logo design contest

```html
<!DOCTYPE html>
<html lang="en">
<head>
<meta charset="utf-8">
<title>Valorix Business Cards</title>
<link href="https://fonts.googleapis.com/css2?family=Cinzel:wght@400;600&family=Open+Sans:wght@400;600;700&display=swap" rel="stylesheet">
<style>
  :root {
    --board: #e9e4dc;
    --card-white: #ffffff;
    --silver-light: #f2f2f2;
    --silver-dark: #a9abae;
    --brand-red: #9b1b1f;
    --deep-red: #5e0b0e;
    --ink: #222222;
    --ink-soft: #444444;
    --band-grey: #6b6d70;
    --label: #3a3632;
  }
  * { margin: 0; padding: 0; box-sizing: border-box; }
  html, body { width: 1200px; height: 794px; overflow: hidden; }
  body { background: var(--board); position: relative; font-family: "Open Sans", sans-serif; }

  .card {
    position: absolute; width: 514px; height: 312px;
    border-radius: 16px; overflow: hidden;
    box-shadow: 0 2px 6px rgba(0,0,0,0.25);
  }
  .card--white { background: var(--card-white); }
  .card--silver { background: radial-gradient(ellipse at 35% 30%, var(--silver-light) 0%, #d4d5d7 55%, var(--silver-dark) 100%); }
  .front-a { left: 79px; top: 43px; }
  .front-b { left: 638px; top: 43px; }
  .back-a  { left: 79px; top: 408px; }
  .back-b  { left: 638px; top: 408px; }

  .brand { position: absolute; left: 17px; top: 40px; display: flex; align-items: center; gap: 8px; }
  .brand__square { width: 18px; height: 18px; background: var(--brand-red); }
  .brand__name {
    font-family: "Open Sans", sans-serif; font-weight: 700; font-size: 26px; line-height: 1;
    color: var(--brand-red);
  }
  .tagline {
    position: absolute; left: 17px; top: 78px;
    font-size: 13px; color: var(--ink);
  }

  .address { position: absolute; left: 17px; top: 190px; font-size: 10px; line-height: 14px; color: var(--ink-soft); }
  .address .key { color: var(--brand-red); font-weight: 700; }
  .address .gap { margin-top: 6px; }

  .person { position: absolute; right: 17px; top: 186px; text-align: right; }
  .person__name { font-weight: 700; font-size: 15px; color: var(--brand-red); }
  .person__title { font-size: 11px; color: var(--ink-soft); }

  .band { position: absolute; left: 0; bottom: 0; width: 514px; height: 66px; }
  .website {
    position: absolute; right: 30px; bottom: 28px;
    font-size: 11px; letter-spacing: 3px; color: #ffffff;
  }

  .back-line {
    position: absolute; inset: 0; display: flex; align-items: center; justify-content: center;
    font-size: 20px; color: var(--ink);
  }

  .label {
    position: absolute; width: 514px; text-align: center;
    font-family: "Cinzel", serif; font-size: 20px; letter-spacing: 2px; color: var(--label);
  }
</style>
</head>
<body>

<section class="card card--white front-a">
  <div class="brand"><span class="brand__square"></span><span class="brand__name">Valorix</span></div>
  <p class="tagline">We keep your project moving</p>
  <div class="address">
    <p>4817 North 52nd Avenue</p>
    <p>Tulsa, OK 74068</p>
    <p class="gap"><span class="key">Phone</span> 918.6273.PRO</p>
    <p><span class="key">Email</span> marla@valorix-example.com</p>
  </div>
  <div class="person"><p class="person__name">Marla Greene</p><p class="person__title">Professional Engineer</p></div>
  <svg class="band" viewBox="0 0 514 66" aria-hidden="true">
    <rect x="0" y="22" width="300" height="14" fill="var(--band-grey)"/>
    <path d="M190 66 C230 40 250 14 300 8 L514 8 L514 66 Z" fill="var(--deep-red)"/>
    <path d="M205 66 C240 44 262 22 310 18 L514 18 L514 66 Z" fill="var(--brand-red)"/>
  </svg>
  <span class="website">www.valorix-example.com</span>
</section>

<section class="card card--silver front-b">
  <div class="brand"><span class="brand__square"></span><span class="brand__name">Valorix</span></div>
  <p class="tagline">We keep your project moving</p>
  <div class="address">
    <p>4817 North 52nd Avenue</p>
    <p>Tulsa, OK 74068</p>
    <p class="gap"><span class="key">Phone</span> 918.6273.PRO</p>
    <p><span class="key">Email</span> marla@valorix-example.com</p>
  </div>
  <div class="person"><p class="person__name">Marla Greene</p><p class="person__title">Professional Engineer</p></div>
  <svg class="band" viewBox="0 0 514 66" aria-hidden="true">
    <rect x="0" y="22" width="300" height="14" fill="var(--band-grey)"/>
    <path d="M190 66 C230 40 250 14 300 8 L514 8 L514 66 Z" fill="var(--deep-red)"/>
    <path d="M205 66 C240 44 262 22 310 18 L514 18 L514 66 Z" fill="var(--brand-red)"/>
  </svg>
  <span class="website">www.valorix-example.com</span>
</section>

<p class="label" style="left:79px; top:368px;">Business Card Front A</p>
<p class="label" style="left:638px; top:368px;">Business Card Front B</p>

<section class="card card--white back-a"><p class="back-line">We keep your project moving</p></section>
<section class="card card--silver back-b"><p class="back-line">We keep your project moving</p></section>

<p class="label" style="left:79px; top:735px;">Business Card Back A</p>
<p class="label" style="left:638px; top:735px;">Business Card Back B</p>

</body>
</html>
```